Ecommerce website Home Page Design that is clean and elegant

Design a Home page for an ecommerce website. This website products and offerings will be very similar to :

brightmeadowtrinkets.com
pebblelanegoods.com

Target Market(s)

Consumer and small shops who can order online.

Industry/Entity Type

Retail

Number of Pages Required

1 page

Colors

Designer to choose colors to be used in the design.

Requirements
Must have
• Exact competition with similar products:
• brightmeadowtrinkets.com
• http://www.pebblelanegoods.com/
• Home page with featured image banner
• List of items on sale or category based items list
• atleast three banners for sale or shipping related offers.
Nice to have
• The logo has very light colors and products will have lots of colors as you can see on competition sites. So the design must consider this so that logo also stands out somewhat for branding purpose.
Should not have
• Design should not have black background

```html
<!DOCTYPE html>
<html lang="en">
<head>
<meta charset="utf-8">
<title>Merrybox — Party Supplies, Candy, Toys &amp; Crafts</title>
<link href="https://fonts.googleapis.com/css2?family=Alegreya:wght@500;700;800&family=Poppins:wght@300;400;500;600&display=swap" rel="stylesheet">
<style>
  :root{
    --rose:#d98fa2;
    --teal:#7fa3ad;
    --ink:#333333;
    --muted:#8a8a8a;
    --gold:#d4a84c;
    --pink:#ec3f8e;
    --lilac:#b29cca;
    --frame:#7ea7b4;
    --paper:#f2f2f2;
    --footer:#2e2e2e;
    --white:#ffffff;
    --serif:'Alegreya', Georgia, serif;
    --sans:'Poppins', Arial, sans-serif;
  }
  *{box-sizing:border-box;margin:0;padding:0}
  html,body{width:1200px;height:2605px;overflow:hidden;background:var(--white)}
  body{position:relative;font-family:var(--sans);color:var(--ink)}
  .abs{position:absolute}
  a{color:inherit;text-decoration:none}

  .promo-strip{left:0;top:0;width:1200px;height:42px;background:var(--rose);color:var(--white);
    font-size:13px;display:flex;align-items:center;justify-content:center;gap:14px;letter-spacing:.2px}

  .brand{left:99px;top:46px;height:52px;display:flex;align-items:center;
    font-family:var(--serif);font-weight:800;font-size:40px;color:var(--rose);letter-spacing:.5px}
  .phone{left:690px;top:56px;width:200px;font-size:22px;color:#3a3a3a;text-align:right;letter-spacing:.5px}
  .header-icons{left:906px;top:42px;height:59px;display:flex}
  .header-icons span{width:64px;height:59px;border-left:1px solid #e4e4e4;display:flex;align-items:center;justify-content:center}
  .header-icons span:last-child{border-right:1px solid #e4e4e4}

  .main-nav{left:99px;top:101px;width:1001px;height:33px;background:var(--teal);display:flex;
    justify-content:space-around;align-items:center;padding:0 60px;color:var(--white);font-size:12px;font-weight:500;letter-spacing:.3px}

  .hero{left:99px;top:134px;width:1001px;height:331px;background:#262626}
  .hero-photo{left:99px;top:134px;width:480px;height:331px;
    background:radial-gradient(circle at 30% 30%,#d9a36a 0,#b5523f 28%,#3b2f2a 62%,#262626 100%)}
  .hero-copy{left:580px;top:236px;width:494px;text-align:center;color:var(--white);
    font-family:var(--serif);font-weight:700;font-size:22px;line-height:42px}
  .btn-outline{border:1.5px solid var(--white);color:var(--white);display:flex;align-items:center;justify-content:center;
    font-size:12px;font-weight:700;letter-spacing:.5px;font-family:var(--serif)}
  .hero-btn{left:745px;top:342px;width:163px;height:35px}

  .tile{top:484px;width:315px;height:172px}
  .tile-clearance{left:99px;background:linear-gradient(135deg,#6b6258,#8a7f72 50%,#4f4740)}
  .tile-toys{left:441px;background:linear-gradient(180deg,#bfe3df 0,#d8efe9 55%,#e8e2d6 100%)}
  .tile-craft{left:785px;background:linear-gradient(135deg,#5a4a3c,#7d6350 50%,#3f342c)}
  .tile-frame{position:absolute;inset:18px;border:1px dashed rgba(255,255,255,.85)}
  .tile-text{position:absolute;left:0;right:0;text-align:center;font-family:var(--serif);font-weight:700}
  .tile-clearance .tile-text{top:52px;color:var(--white);font-size:23px;line-height:40px}
  .tile-toys .tile-text{top:50px;left:140px;right:10px;color:#4a4a4a;font-size:22px;line-height:36px}
  .tile-craft .tile-text{top:40px;color:var(--white);font-size:25px;line-height:36px}
  .tile-craft small{display:block;font-family:var(--serif);font-size:12px;line-height:20px;letter-spacing:.4px}
  .tile-toys .tile-photo{position:absolute;left:0;top:0;width:170px;height:172px;background:linear-gradient(180deg,#c7a07c,#e9e2d2)}

  .wedding{left:96px;top:695px;width:1004px;height:243px;
    background:linear-gradient(90deg,#a07c72 0,#c4a094 35%,#d9c2b4 65%,#9b8e88 100%)}
  .wedding-title{left:146px;top:736px;font-family:var(--serif);font-weight:700;font-size:33px;color:var(--white)}
  .wedding-off{left:146px;top:792px;font-family:var(--serif);font-weight:800;font-size:38px;color:var(--white)}
  .wedding-btn{left:146px;top:863px;width:231px;height:38px;font-size:17px}

  .tab-active{left:99px;top:976px;width:148px;height:31px;background:var(--gold);color:var(--white);
    font-family:var(--serif);font-size:18px;display:flex;align-items:center;justify-content:center}
  .tab{left:267px;top:978px;font-family:var(--serif);font-size:19px;color:#444}
  .tab-rule{left:99px;top:1020px;width:1001px;height:2px;background:#e1e1e1}
  .tab-dots{left:1065px;top:991px;display:flex;gap:3px}
  .tab-dots i{width:7px;height:7px;border-radius:50%;border:1.5px solid #9a9a9a;display:block}

  .product{top:1051px;width:238px}
  .product-photo{height:251px;position:relative}
  .product-meta{display:flex;justify-content:space-between;font-size:14px;color:#444;margin-top:16px}
  .p1{left:99px}.p2{left:353px}.p3{left:606px}.p4{left:861px}
  .p1 .product-photo{background:linear-gradient(180deg,#5cc0e3 0,#a9dcec 60%,#e8f3f7 100%)}
  .p2 .product-photo{background:linear-gradient(160deg,#c7a19a,#a98680 60%,#8e716b)}
  .p3 .product-photo{background:radial-gradient(circle at 50% 50%,#4ec3c6 0,#8fd6d7 22%,#fff 45%);border:1px solid #e6e6e6}
  .p4 .product-photo{background:linear-gradient(160deg,#f4ede4,#b9aca0 45%,#3a3532 80%)}
  .cart-btn{position:absolute;left:36px;top:124px;width:166px;height:34px;font-family:var(--sans);font-weight:500;font-size:13px;letter-spacing:1px}

  .candy{left:96px;top:1370px;width:1004px;height:243px;
    background:linear-gradient(100deg,#8fd0dd 0,#e8f3f6 30%,#f3c6d6 55%,#a9d8e3 80%,#f1b3c8 100%)}
  .candy-frame{left:130px;top:1398px;width:928px;height:193px;border:2.5px solid var(--pink)}
  .candy-title{left:130px;top:1422px;width:928px;text-align:center;font-family:var(--serif);font-weight:700;font-size:33px;line-height:46px;color:var(--pink)}
  .candy-off{left:130px;top:1474px;width:928px;text-align:center;font-family:var(--serif);font-weight:800;font-size:40px;line-height:48px;color:var(--pink)}
  .candy-btn{left:483px;top:1530px;width:229px;height:38px;background:var(--pink);color:var(--white);
    font-family:var(--serif);font-weight:700;font-size:18px;display:flex;align-items:center;justify-content:center;letter-spacing:.4px}

  .ship-frame{left:115px;top:1683px;width:536px;height:305px;border:2px solid var(--frame)}
  .ship-photo{left:563px;top:1662px;width:529px;height:354px;
    background:linear-gradient(180deg,#8e8c88 0,#a5a29d 40%,#4fa3d6 62%,#f08a3c 80%,#e55c8f 100%)}
  .ship-copy{left:140px;top:1742px;width:404px;text-align:center;font-family:var(--serif);color:#555}
  .ship-title{font-size:32px;font-weight:700;line-height:46px}
  .ship-orders{font-size:24px;font-weight:700;line-height:44px}
  .ship-code{font-family:var(--sans);font-size:21px;text-decoration:underline;line-height:40px}
  .ship-btn{left:247px;top:1898px;width:192px;height:30px;background:var(--lilac);color:var(--white);
    font-size:15px;font-weight:500;letter-spacing:.8px;display:flex;align-items:center;justify-content:center}

  .disclaimer{left:0;top:2073px;width:1200px;height:165px;background:var(--paper)}
  .disclaimer h4{position:absolute;left:111px;top:30px;font-size:14px;font-weight:600;color:#555}
  .disclaimer p{position:absolute;left:111px;top:58px;width:970px;font-size:10.5px;line-height:20px;color:#9a9a9a}

  .site-footer{left:0;top:2238px;width:1200px;height:367px;background:var(--footer);color:var(--white)}
  .f-col{position:absolute;top:44px}
  .f-col h5{font-size:16px;font-weight:600;margin-bottom:22px}
  .f-col li{list-style:none;font-size:13px;line-height:29px;display:flex;align-items:center;gap:8px}
  .f-col li i{width:14px;height:14px;border-radius:50%;border:1.5px solid var(--white);display:block}
  .c1{left:104px}.c2{left:361px}.c3{left:570px}.c4{left:806px}.c5{left:992px}
  .cards{position:absolute;left:101px;top:284px;display:flex;gap:10px}
  .cards span{width:36px;height:24px;background:var(--white);border-radius:2px;display:block}
  .newsletter-label{position:absolute;left:866px;top:248px;font-size:13px;font-weight:600}
  .newsletter{position:absolute;left:866px;top:278px;width:228px;height:32px;background:var(--white);display:flex;align-items:center}
  .newsletter span{flex:1;font-size:11px;color:#777;padding-left:10px}
  .newsletter b{width:36px;height:32px;display:flex;align-items:center;justify-content:center}
  .copyright{position:absolute;left:0;right:0;top:338px;text-align:center;font-size:12px}
  .back-top{position:absolute;left:1038px;top:334px;font-size:12px;display:flex;align-items:center;gap:6px}
</style>
</head>
<body>

<div class="abs promo-strip"><span>Catalog Quick Order</span><span>|</span><span>110% Lowest Price Guarantee</span><span>|</span><span>100% Happiness Guarantee</span></div>

<header>
  <div class="abs brand">Merrybox</div>
  <div class="abs phone">1-800-555-0142</div>
  <div class="abs header-icons">
    <span><svg width="22" height="22" viewBox="0 0 24 24" fill="none" stroke="#333" stroke-width="1.6"><circle cx="12" cy="8" r="4"/><path d="M4 21c0-4.4 3.6-7 8-7s8 2.6 8 7z"/></svg></span>
    <span><svg width="22" height="22" viewBox="0 0 24 24" fill="none" stroke="#333" stroke-width="1.8"><circle cx="10" cy="10" r="6.5"/><path d="M15 15l6 6"/></svg></span>
    <span><svg width="20" height="22" viewBox="0 0 24 24" fill="none" stroke="#333" stroke-width="1.6"><rect x="4" y="7" width="16" height="15"/><path d="M8 10V5a4 4 0 0 1 8 0v5"/></svg></span>
  </div>
  <nav class="abs main-nav"><a>PARTY SUPPLIES</a><a>OCCASIONS AND EVENTS</a><a>TOYS AND GAMES</a><a>CRAFTS</a><a>WEDDING HOLIDAYS</a></nav>
</header>

<section>
  <div class="abs hero"></div>
  <div class="abs hero-photo" role="img" aria-label="Bowls of colourful candies, marshmallows and swirl lollipops on a dark slate"></div>
  <div class="abs hero-copy">Find Nostalgic Candy And All The Sweet Treats<br>You Need In Our One-Stop Candy Shop!</div>
  <a class="abs btn-outline hero-btn">SHOP NOW &gt;&gt;</a>
</section>

<section>
  <div class="abs tile tile-clearance" role="img" aria-label="Summer party props on a wooden table">
    <div class="tile-frame"></div>
    <div class="tile-text">SUMMER CLEARANCE<br>upto 60% off</div>
  </div>
  <div class="abs tile tile-toys">
    <div class="tile-photo" role="img" aria-label="Plush teddy bears in a white wicker basket"></div>
    <div class="tile-text">TOYS GAMES<br><span style="font-size:16px">upto 40% off</span></div>
  </div>
  <div class="abs tile tile-craft" role="img" aria-label="Scrapbooking supplies and paper crafts on a desk">
    <div class="tile-frame"></div>
    <div class="tile-text">Scrapbooking<br>&amp; Paper Crafting<small>SHOP NOW &gt;&gt;</small></div>
  </div>
</section>

<section>
  <div class="abs wedding" role="img" aria-label="Wedding cake with a couple topper on a soft blurred background"></div>
  <div class="abs wedding-title">Celebrate Your Big Day With Unique Wedding Ideas</div>
  <div class="abs wedding-off">30% OFF</div>
  <a class="abs btn-outline wedding-btn">SHOP ALL TODAY</a>
</section>

<section>
  <div class="abs tab-active">Top Products</div>
  <div class="abs tab">Clearance Sale</div>
  <div class="abs tab-dots"><i></i><i></i><i></i><i></i></div>
  <div class="abs tab-rule"></div>

  <div class="abs product p1"><div class="product-photo" role="img" aria-label="Glass jar full of colourful jelly beans"></div><div class="product-meta"><span>Candy</span><span>$ 23.00</span></div></div>
  <div class="abs product p2"><div class="product-photo" role="img" aria-label="Wooden craft tools in a glass jar with twine"><a class="btn-outline cart-btn">ADD TO CART</a></div><div class="product-meta"><span>Craft</span><span>$ 23.00</span></div></div>
  <div class="abs product p3"><div class="product-photo" role="img" aria-label="Plush toy dragon"></div><div class="product-meta"><span>Toys</span><span>$ 23.00</span></div></div>
  <div class="abs product p4"><div class="product-photo" role="img" aria-label="Game controller resting on a keyboard"></div><div class="product-meta"><span>Games</span><span>$ 23.00</span></div></div>
</section>

<section>
  <div class="abs candy" role="img" aria-label="Pastel pink and blue watercolour wash"></div>
  <div class="abs candy-frame"></div>
  <div class="abs candy-title">Flavorful Chewy Candy And Holiday Candy</div>
  <div class="abs candy-off">30% OFF</div>
  <a class="abs candy-btn">SHOP ALL CANDY</a>
</section>

<section>
  <div class="abs ship-photo" role="img" aria-label="Colourful pencils in a cup beside notebooks and markers on a grey wooden table"></div>
  <div class="abs ship-frame"></div>
  <div class="abs ship-copy">
    <div class="ship-title">Free Shipping&nbsp; $10 Off</div>
    <div class="ship-orders">Orders $ 88+</div>
    <div class="ship-code">Use Code SHIP</div>
  </div>
  <a class="abs ship-btn">SHOP NOW</a>
</section>

<section class="abs disclaimer">
  <h4>Disclaimer</h4>
  <p>Our prices, stock levels and promotions may change without notice. Product colours can vary slightly from how they appear on your screen. Discount codes apply to eligible items only and cannot be combined with other offers unless stated. Free shipping covers standard delivery within the contiguous states. Bulk orders for shops and events may require extra processing time. Please review item details, sizes and age guidance before buying. Returns are accepted on unused goods within thirty days of delivery, in original packaging, with proof of purchase from our store.</p>
</section>

<footer class="abs site-footer">
  <div class="f-col c1"><h5>Why Shop With Us</h5><ul><li>Shopping</li><li>Payment</li><li>Delivery</li><li>Returns &amp; Exchange</li></ul></div>
  <div class="f-col c2"><h5>Sell With Us</h5><ul><li>Why Join Us</li><li>Benefits</li><li>Open A Shop</li><li>Seller Guide</li></ul></div>
  <div class="f-col c3"><h5>Get To Know Us</h5><ul><li>About Us</li><li>Contact Us</li><li>Terms Of Use</li><li>Privacy</li><li>FAQ's</li></ul></div>
  <div class="f-col c4"><h5>Follow Us</h5><ul><li><i></i>Circlefeed</li><li><i></i>Snapreel</li><li><i></i>Chirpline</li><li><i></i>Ideaboard</li><li><i></i>Clipstream</li></ul></div>
  <div class="f-col c5"><h5>My Account</h5><ul><li>Cart</li><li>My Account</li><li>Checkout</li><li>Wishlist</li><li>Login/Register</li></ul></div>

  <div class="cards"><span></span><span></span><span></span><span></span></div>

  <div class="newsletter-label">Sign Up For Newsletter</div>
  <div class="newsletter"><span>Email Address</span><b><svg width="18" height="14" viewBox="0 0 18 14"><rect width="18" height="14" rx="1" fill="#222"/><path d="M1 1l8 6 8-6" fill="none" stroke="#fff" stroke-width="1.4"/></svg></b></div>

  <div class="copyright">© 2017 Merrybox. All Rights Reserved.</div>
  <div class="back-top">Back To Top <svg width="14" height="14" viewBox="0 0 14 14" fill="none" stroke="#fff" stroke-width="1.3"><circle cx="7" cy="7" r="6"/><path d="M4 7h6M7.5 4.5L10 7 7.5 9.5"/></svg></div>
</footer>

</body>
</html>
```